Oven Cleaning Business owner needs business card design

Hi there,
Would like for a business card to be designed for myself, the owner of a professional oven cleaning business on the Sunshine Coast.
Would like it to look sleek, and modern-ish. Bit creative is encouraged too.
Include following:
Name/title: Corin ter Haghe, Owner
Phone number: 1300 482 916
Email: info@hearthshinecrew.com.au
Website: www.hearthshinecrew.com.au

```html
<!DOCTYPE html>
<html lang="en">
<head>
<meta charset="utf-8">
<title>Hearthshine Crew – Business Card</title>
<link rel="stylesheet" href="https://fonts.googleapis.com/css2?family=Archivo:wght@700;800&family=Arimo:wght@400&display=swap">
<style>
  :root {
    --bg: #2a2a2c;
    --teal: #17c9cc;
    --ink: #111214;
    --paper: #fbfbfb;
    --muted: #333;
  }
  * { margin: 0; padding: 0; box-sizing: border-box; }
  html, body {
    width: 1200px; height: 779px; overflow: hidden;
    background: var(--bg);
  }
  .canvas { position: relative; width: 1200px; height: 779px; }

  .card {
    position: absolute;
    width: 520px; height: 300px;
    box-shadow: 0 10px 24px rgba(0,0,0,.45);
  }

  /* Front */
  .card-front {
    left: 70px; top: 80px;
    background: var(--teal);
    display: flex; align-items: center; justify-content: center;
  }
  .front-brand {
    font-family: "Archivo", sans-serif;
    font-weight: 800;
    font-size: 40px;
    letter-spacing: 1px;
    text-transform: uppercase;
    color: var(--ink);
  }

  /* Back */
  .card-back {
    left: 610px; top: 400px;
    background: var(--paper);
  }
  .back-brand {
    position: absolute; left: 150px; top: 78px;
    display: flex; align-items: center; gap: 10px;
  }
  .brand-dot {
    width: 34px; height: 34px; border-radius: 50%;
    background: var(--teal);
  }
  .back-brand-name {
    font-family: "Archivo", sans-serif;
    font-weight: 800;
    font-size: 22px;
    text-transform: uppercase;
    color: var(--ink);
  }
  .person {
    position: absolute; right: 296px; top: 150px;
    text-align: right;
  }
  .person-name {
    font-family: "Archivo", sans-serif;
    font-weight: 800; font-size: 19px; color: var(--ink);
    white-space: nowrap;
  }
  .person-title {
    font-family: "Arimo", sans-serif;
    font-size: 15px; color: var(--teal); margin-top: 2px;
  }
  .divider {
    position: absolute; left: 238px; top: 136px;
    width: 1.5px; height: 72px; background: var(--ink);
  }
  .contacts {
    position: absolute; left: 254px; top: 138px;
    list-style: none;
    font-family: "Arimo", sans-serif; font-size: 13.5px; color: var(--muted);
  }
  .contacts li { display: flex; align-items: center; gap: 8px; height: 22px; }
  .contacts svg { width: 12px; height: 12px; fill: var(--teal); flex: none; }
</style>
</head>
<body>
<main class="canvas">
  <section class="card card-front" aria-label="Card front">
    <div class="front-brand">Hearthshine Crew</div>
  </section>

  <section class="card card-back" aria-label="Card back">
    <div class="back-brand">
      <span class="brand-dot"></span>
      <span class="back-brand-name">Hearthshine Crew</span>
    </div>

    <div class="person">
      <div class="person-name">Corin ter Haghe</div>
      <div class="person-title">Owner</div>
    </div>

    <div class="divider"></div>

    <ul class="contacts">
      <li>
        <svg viewBox="0 0 24 24" aria-hidden="true"><path d="M6.6 10.8a15.1 15.1 0 0 0 6.6 6.6l2.2-2.2a1 1 0 0 1 1-.25 11.4 11.4 0 0 0 3.6.57 1 1 0 0 1 1 1V20a1 1 0 0 1-1 1A17 17 0 0 1 3 4a1 1 0 0 1 1-1h3.5a1 1 0 0 1 1 1c0 1.25.2 2.45.57 3.6a1 1 0 0 1-.25 1z"/></svg>
        1300 482 916
      </li>
      <li>
        <svg viewBox="0 0 24 24" aria-hidden="true"><path d="M2 5h20v14H2z M4 7v.5l8 5 8-5V7l-8 5z" fill-rule="evenodd"/></svg>
        info@hearthshinecrew.com.au
      </li>
      <li>
        <svg viewBox="0 0 24 24" aria-hidden="true"><circle cx="12" cy="12" r="10"/></svg>
        www.hearthshinecrew.com.au
      </li>
    </ul>
  </section>
</main>
</body>
</html>
```